Meadowlark Counseling Partners, LLC Needs Modern Business Card Design.

We provide behavioral health services from western Kansas to eastern Kansas. There is an abundance of competition for the services we provide with our main competitor being larger and having significantly more financial resources; however, the quality of services we provide is greater and we have started to catch the attention of the State of Kansas. We had a great logo designed by ArtFolio - this will be used to build upon our brand. The logo (attached) should be used in the card development. We want something unique, modern, but also a card design that clearly states our name, contact info, provides the name and unqiue location of each clinician, etc. Rounded edges, or a unique size, just something that makes our business card stand out from others. I have also uploaded each clinician's name and their unique location and phone number.

Our idea is to have one side be black with our logo. Then, on the other side have business cards for each individual. Plus, we want one card that is "generic" with no specific clinician's name listed so that we can give clients an appointment card when they leave. Some clinicians have two locations - we're open to design and background color, but we have started going with branding colors of black, the yellow in the logo files attached, and sometimes a gray. Our new office has been decorated using this theme.

Target Market(s)

individuals and families in need of behavioral health services; potential professional referral sources; existing referral sources

Industry/Entity Type

Business

Contact Information for Business Card

I attached a Word doc that provides clinician names, credentials and location information specific to each individual.

Font styles to use
Serif

Colors
000000
fbed22
dbdbdb
9d9d9d
c3c3c3

Requirements
Must have
• 1) use of the company logo that has been attached; 2) a template that provides us space to individualize business cards for all of our clinicians; 3) should stick to the colors we are branding with: black, yellow from the logo file, maybe a gray shade and we're open to a suggestion on a shade of white.
Nice to have
• Group discussion culminated in the thought that one side would be black with just our logo - no clinician names, etc. A unique design - rounded edges, unique size, some catchy lay-out would be nice.
Should not have
• Must not be too busy. Should look "clean." The project should stick to branding colors: black, yellow (from the logo file), maybe a gray and shade of white.

```html
<!DOCTYPE html>
<html lang="en">
<head>
<meta charset="utf-8">
<title>Meadowlark Counseling Partners — Business Card</title>
<link href="https://fonts.googleapis.com/css2?family=Cinzel:wght@600&family=Kanit:wght@300;500&display=swap" rel="stylesheet">
<style>
  :root {
    --page: #e9e7e3;
    --yellow-light: #fde60f;
    --yellow-deep: #f9b71b;
    --amber: #f6ad1c;
    --cream: #fbefd2;
    --ink: #2b2b2b;
    --ink-soft: #4a4a4a;
    --rule: #6d6d6d;
    --paper: #ffffff;
  }
  * { box-sizing: border-box; margin: 0; padding: 0; }
  html, body { width: 1200px; height: 1200px; overflow: hidden; }
  body {
    background: var(--page);
    display: flex;
    flex-direction: column;
    align-items: center;
    justify-content: center;
    gap: 56px;
  }
  .card {
    position: relative;
    width: 900px;
    height: 514px;
    overflow: hidden;
    box-shadow: 0 6px 18px rgba(0,0,0,0.12);
  }

  /* Front */
  .card--front {
    background: linear-gradient(200deg, var(--yellow-light) 0%, #fdd414 45%, var(--yellow-deep) 100%);
  }
  .card--front .decor {
    position: absolute;
    left: -60px; bottom: -120px;
    width: 720px; height: 520px;
    border-radius: 50% 50% 0 0;
    background: radial-gradient(ellipse at 45% 80%, rgba(246,160,20,0.55) 0%, rgba(248,178,24,0.35) 45%, rgba(253,214,20,0) 75%);
  }
  .card--front .brand {
    position: absolute;
    left: 210px; top: 170px;
    font-family: "Cinzel", serif;
    font-weight: 600;
    color: var(--ink);
    text-align: center;
  }
  .brand__name { display: block; font-size: 58px; letter-spacing: 4px; line-height: 1; }
  .brand__sub { display: block; font-size: 22px; letter-spacing: 2.5px; margin-top: 10px; }

  /* Back */
  .card--back { background: var(--paper); }
  .card--back .decor {
    position: absolute;
    left: -20px; bottom: -80px;
    width: 700px; height: 430px;
    border-radius: 50% 50% 0 0;
    background: radial-gradient(ellipse at 45% 85%, var(--cream) 0%, rgba(251,239,210,0.7) 45%, rgba(255,255,255,0) 75%);
  }
  .card--back .brand {
    position: absolute;
    left: 70px; top: 150px;
    width: 440px;
    font-family: "Cinzel", serif;
    font-weight: 600;
    color: var(--amber);
    text-align: center;
  }
  .card--back .brand__name { font-size: 46px; letter-spacing: 3px; }
  .card--back .brand__sub { font-size: 17px; letter-spacing: 1.8px; margin-top: 8px; }
  .card--back .brand__dot {
    display: block;
    width: 44px; height: 44px;
    margin: 0 auto 20px;
    border-radius: 50%;
    background: var(--amber);
  }
  .divider {
    position: absolute;
    left: 540px; top: 120px;
    width: 1px; height: 240px;
    background: var(--rule);
  }
  .contact {
    position: absolute;
    left: 568px; top: 118px;
    font-family: "Kanit", sans-serif;
    color: var(--ink-soft);
  }
  .contact__name { font-weight: 500; font-size: 32px; color: var(--ink-soft); letter-spacing: 0.3px; }
  .contact__title { font-weight: 300; font-size: 20px; margin-top: 2px; }
  .contact__lines { list-style: none; margin-top: 22px; font-weight: 300; font-size: 21px; line-height: 1.45; }
</style>
</head>
<body>
  <section class="card card--front" aria-label="Card front">
    <div class="decor" role="img" aria-label="Large sunflower illustration in warm yellow tones"></div>
    <h1 class="brand">
      <span class="brand__name">MEADOWLARK</span>
      <span class="brand__sub">COUNSELING PARTNERS, LLC</span>
    </h1>
  </section>

  <section class="card card--back" aria-label="Card back">
    <div class="decor" role="img" aria-label="Faint sunflower illustration in pale cream"></div>
    <div class="brand">
      <span class="brand__dot"></span>
      <span class="brand__name">MEADOWLARK</span>
      <span class="brand__sub">COUNSELING PARTNERS, LLC</span>
    </div>
    <div class="divider"></div>
    <div class="contact">
      <p class="contact__name">GREGORY T. HOLLIS, LP</p>
      <p class="contact__title">President</p>
      <ul class="contact__lines">
        <li>(316) 555-0148</li>
        <li>418 N. Prairie Ave.</li>
        <li>Wichita, Kansas 67202</li>
      </ul>
    </div>
  </section>
</body>
</html>
```